依頼概要
■依頼の目的/概要
弊社では有機栽培の梅の通販を行うサイトの運営をしております。
5月・6月限定での販売の生梅を使った梅酒・梅干し・梅シロップのレシピ依頼
当店オリジナルデザインのレシピ集のデザインをお願いします。
サイズA4サイズ 手書き風 下記3種類
・梅シロップの作り方
・梅酒の作り方
・梅干しの作り方

■依頼詳細
弊社のロゴを入れた手書き風のレシピ集デザインをお願いします。
30代のお子さんをお持ちのお母さんをターゲットとしております。
当店のイメージ【まどろみ柚子堂】に沿ったものにしていただきたいです。

■重視する点
過去・現在までにデザインの経験がある方がのぞましいです。

その他何かご不明な点がございましたら、お気軽にご質問下さい。
よろしくお願いいたします。

有機梅干し専門店 まどろみ柚子堂
有限会社 桐谷果樹園
桐谷 蒼
http://www.madoromi-yuzudo.jp/
A4サイズとありますが、デザイン重視でサイズは気にしなくてもかまいません。【B5やA5でもOKです】

梅シロップ・・・1枚
梅酒レシピ・・・1枚
梅干しレシピ・・・1枚

合計3枚となります。
イラストや手書き風の絵が希望です。

写真はあまり使用したくありません。

当社名が”まどろみ柚子堂”になりますのでやさしい雰囲気を希望しております。

無農薬・無肥料栽培の梅干し専門の為。
当社ロゴデータになります。

PDFデータです。

どちらかのロゴを使用して頂ければとおもいます。
デザインのサイズについて、A4、A5、B5など両面の場合、半分に折って見開きのデザインもOKです。
■ 選んだ理由

受け取ったお客様が喜んでくれそうな工夫です。

温かみのあるデザインにスタッフ一同喜んでおります。

■ 提案者全員のお礼・コメント

ほんとうにありがとうございます。

大変質のよいデザインに本当に嬉しく思います。

```html
<!DOCTYPE html>
<html lang="ja">
<head>
<meta charset="utf-8">
<title>梅干しのレシピ</title>
<link rel="stylesheet" href="https://fonts.googleapis.com/css2?family=Shippori+Mincho:wght@400;600&display=swap">
<style>
  :root {
    --paper: #ffffff;
    --ink: #3b3a36;
    --ink-soft: #6a6862;
    --rule: #cfcfcf;
    --plum-green: #c9d66a;
    --plum-pale: #eef2c8;
    --glass: #e8ece8;
    --salt: #e9e7e2;
    --wood: #e6d3a8;
    --umeboshi: #d9894f;
    --plate: #f3eee4;
    --badge: #7d9a4a;
  }
  * { box-sizing: border-box; margin: 0; padding: 0; }
  html, body { width: 859px; height: 1200px; overflow: hidden; background: var(--paper); }
  body { font-family: "Shippori Mincho", serif; color: var(--ink); }

  .spread { position: relative; width: 859px; height: 1200px; display: flex; }
  .panel { position: relative; width: 50%; height: 100%; }
  .panel--inside { border-right: 1px solid var(--rule); }

  .tools-heading { position: absolute; left: 40px; top: 30px; font-size: 13px; font-weight: 600; letter-spacing: .05em; }

  .item { position: absolute; }
  .item__art { display: block; }
  .item__name { font-size: 11px; font-weight: 600; margin-top: 8px; border-bottom: 1px solid var(--ink-soft); display: inline-block; padding-bottom: 2px; }
  .item__note { font-size: 9.5px; line-height: 1.6; color: var(--ink-soft); margin-top: 5px; }

  .item--plum { left: 40px; top: 60px; width: 190px; }
  .item--jar { left: 262px; top: 58px; width: 150px; }
  .item--salt { left: 40px; top: 262px; width: 190px; }
  .item--skewer { left: 262px; top: 292px; width: 150px; }

  .divider { position: absolute; left: 40px; right: 40px; top: 440px; border-top: 1px solid var(--rule); }

  .intro { position: absolute; left: 40px; right: 40px; top: 475px; font-size: 12.5px; line-height: 2.05; letter-spacing: .03em; text-align: justify; }

  .cert { position: absolute; left: 52px; top: 1060px; width: 70px; text-align: center; }
  .cert__note { font-size: 7px; line-height: 1.5; color: var(--ink-soft); margin-top: 6px; white-space: nowrap; }

  .brand { position: absolute; left: 0; right: 0; top: 40px; text-align: center; }
  .brand__name { font-size: 14px; font-weight: 600; letter-spacing: .15em; }
  .brand__art { display: block; margin: 8px auto 0; }

  .title { position: absolute; left: 0; right: 0; top: 232px; text-align: center; }
  .title__main { font-size: 27px; font-weight: 600; letter-spacing: .08em; }
  .title__sub { font-size: 10px; letter-spacing: .1em; color: var(--ink-soft); margin-top: 6px; }

  .hero { position: absolute; left: 80px; top: 345px; }

  .tagline { position: absolute; left: 0; right: 0; top: 915px; text-align: center; font-size: 13px; line-height: 2; letter-spacing: .06em; }
</style>
</head>
<body>
<main class="spread">
  <section class="panel panel--inside">
    <h2 class="tools-heading">用意する材料や道具</h2>

    <div class="item item--plum">
      <svg class="item__art" width="180" height="110" role="img" aria-label="青々とした完熟生梅の実のイラスト"><rect width="180" height="110" rx="40" fill="var(--plum-green)" opacity=".55"/></svg>
      <p class="item__name">オーガニックの完熟生梅 / 1kg</p>
      <p class="item__note">まどろみ柚子堂で収穫している、<br>オーガニックな完熟生梅です。</p>
    </div>

    <div class="item item--jar">
      <svg class="item__art" width="80" height="120" role="img" aria-label="ふた付きのガラス保存瓶のイラスト"><rect width="80" height="120" rx="14" fill="var(--glass)"/></svg>
      <p class="item__name">漬けるための保存瓶</p>
      <p class="item__note">スーパーやホームセンターで販売されているものでOK。容器に入れる前によく洗って、しっかり乾かしてからご使用ください。</p>
    </div>

    <div class="item item--salt">
      <svg class="item__art" width="170" height="90" role="img" aria-label="山盛りの粗塩のイラスト"><rect width="170" height="90" rx="36" fill="var(--salt)"/></svg>
      <p class="item__name">海水塩（粗塩）/200g</p>
      <p class="item__note">梅干しを漬ける粗塩です。自然塩を使うのがおすすめです。精製塩よりもまろやかな味わいになり、梅の風味がよく引き立ちます。</p>
    </div>

    <div class="item item--skewer">
      <svg class="item__art" width="100" height="32" role="img" aria-label="竹串と爪楊枝のイラスト"><rect width="100" height="32" rx="8" fill="var(--wood)" opacity=".6"/></svg>
      <p class="item__name">竹串や爪楊枝</p>
      <p class="item__note">ヘタを取り除くときに使います。</p>
    </div>

    <div class="divider"></div>

    <p class="intro">オーガニック完熟梅を使って作る、梅干しの作り方を紹介しました。梅干しは昔ほど家で漬けられなくなり、有機栽培の農家を探して完熟梅を手に入れることも難しくなりました。柔らかい梅干しにするコツは、完熟前の固い梅ではなく黄色く熟した梅を使うこと。手間はかかりますが、一粒ずつ丁寧に漬けた梅干しは格別です。余計なものは入れず、梅と塩だけで作る昔ながらの酸っぱい梅干しです。保存がきくので、家族みんなで長く楽しめます。</p>

    <div class="cert">
      <svg width="54" height="62" role="img" aria-label="有機認証マーク"><circle cx="27" cy="27" r="24" fill="none" stroke="var(--badge)" stroke-width="2"/></svg>
      <p class="cert__note">有機認証取得農園<br>認定番号 0000-00</p>
    </div>
  </section>

  <section class="panel panel--cover">
    <div class="brand">
      <p class="brand__name">まどろみ柚子堂</p>
      <svg class="brand__art" width="130" height="130" role="img" aria-label="梅の枝が入ったマグカップのイラスト"><rect width="130" height="130" rx="20" fill="var(--plum-pale)"/></svg>
    </div>

    <div class="title">
      <h1 class="title__main">梅干しのレシピ</h1>
      <p class="title__sub">Recipe for pickled plums</p>
    </div>

    <svg class="hero" width="270" height="260" role="img" aria-label="白い皿に盛られた梅干しの写真">
      <defs>
        <radialGradient id="plateGlow" cx="50%" cy="50%" r="55%">
          <stop offset="0%" stop-color="var(--umeboshi)"/>
          <stop offset="45%" stop-color="#e8a878"/>
          <stop offset="70%" stop-color="var(--plate)"/>
          <stop offset="100%" stop-color="var(--paper)"/>
        </radialGradient>
      </defs>
      <ellipse cx="135" cy="130" rx="130" ry="125" fill="url(#plateGlow)"/>
    </svg>

    <p class="tagline">オーガニックの完熟生梅と塩のみで作る、<br>昔ながらの酸っぱい梅干しです。</p>
  </section>
</main>
</body>
</html>
```